Quillon Energy Business Cards

I would like to design some options for about 10 sets of double sided business cards for our team with a raised logo with a Silver glossy finished logo. We are a privately funded upstream Oil & Gas producer drilling vertical wells in Central Oklahoma with a long term production (ROI driven) strategy that we implement through an annual drilling program. We are focused on a shallow / vertical / long life / low decline strategy. We are based in downtown Tulsa Oklahoma. I have attached a sample business card and a picture of our hallway logo which we would like to replicate on the business cards.

Target Market(s)

BRQ Accredited Investors and other Oil & Gas Operators

Industry/Entity Type

Upstream Oil & Gas

Contact Information for Business Card

You can see the sample photo attached, but email / website / address / direct phone / Cell Phone / Name / Title / Fax

Font styles to use
Other font styles liked:
• Felix Titling

Colors
0054AA
0677BA
7BADD7
CADEEF
E8F1F8

Requirements
Must have
• Glossy raised logo
Nice to have
• Possibly a new logo.
Should not have
• No Greens /

```html
<!DOCTYPE html>
<html lang="en">
<head>
<meta charset="utf-8">
<title>Quillon Energy Business Card</title>
<link href="https://fonts.googleapis.com/css2?family=Tinos:wght@400;700&display=swap" rel="stylesheet">
<style>
  :root {
    --stage: #232323;
    --card: #1f1f22;
    --card-deep: #161618;
    --gold: #e3b21c;
    --gold-soft: #c9981a;
    --ink: #f2f2f2;
    --pattern-light: #3a3a3e;
  }
  * { box-sizing: border-box; margin: 0; padding: 0; }
  html, body { width: 1200px; height: 780px; overflow: hidden; }
  body {
    background: var(--stage);
    font-family: "Tinos", "Times New Roman", serif;
    position: relative;
  }
  .card {
    position: absolute;
    top: 80px;
    width: 360px;
    height: 620px;
    background: var(--card);
    border: 2px solid var(--gold);
    overflow: hidden;
  }
  .card--back {
    left: 200px;
    border-radius: 180px 180px 0 0;
  }
  .card--front {
    left: 640px;
    border-radius: 0 0 180px 180px;
  }
  .back-texture {
    position: absolute;
    inset: 0;
    background: radial-gradient(circle at 30% 30%, var(--pattern-light), var(--card-deep) 75%);
  }
  .back-mark {
    position: absolute;
    top: 120px;
    right: 60px;
    font-size: 8px;
    letter-spacing: 0.08em;
    color: var(--gold);
  }
  .company {
    position: absolute;
    top: 60px;
    left: 0;
    right: 0;
    text-align: center;
    color: var(--gold);
    font-size: 22px;
    letter-spacing: 0.06em;
  }
  .company-dot {
    display: block;
    width: 14px;
    height: 14px;
    margin: 0 auto 14px;
    border-radius: 50%;
    background: var(--gold);
  }
  .details {
    position: absolute;
    top: 240px;
    left: 40px;
    right: 30px;
    text-align: center;
    color: var(--ink);
  }
  .person-name {
    color: var(--gold);
    font-weight: 700;
    font-size: 20px;
    letter-spacing: 0.02em;
  }
  .person-title {
    font-size: 11px;
    line-height: 1.35;
    margin-top: 4px;
  }
  .address {
    font-size: 15px;
    line-height: 1.3;
    margin-top: 26px;
  }
  .contacts {
    list-style: none;
    margin-top: 24px;
    text-align: left;
    display: inline-block;
    font-size: 15px;
    line-height: 1.5;
  }
  .contacts li { display: flex; align-items: center; gap: 10px; }
  .contacts svg { width: 13px; height: 13px; fill: var(--gold); flex: none; }
</style>
</head>
<body>
  <section class="card card--back">
    <div class="back-texture" role="img" aria-label="Embossed repeating pattern of dark raised marks"></div>
    <span class="back-mark">QUILLON ENERGY, LLC</span>
  </section>

  <section class="card card--front">
    <div class="company">
      <span class="company-dot"></span>
      QUILLON ENERGY, LLC
    </div>
    <div class="details">
      <p class="person-name">DORIAN K. VASSELT, CPL</p>
      <p class="person-title">EXECUTIVE VICE PRESIDENT<br>LAND, LEGAL &amp; BUSINESS DEVELOPMENT</p>
      <p class="address">42 NORTH 9TH ST SUITE 800<br>TULSA, OK 74103</p>
      <ul class="contacts">
        <li><svg viewBox="0 0 16 16"><path d="M3 1l3 3-2 2c1 2 3 4 5 5l2-2 3 3-2 3C7 15 1 9 0 4z"/></svg>539-555-0142 (Direct)</li>
        <li><svg viewBox="0 0 16 16"><path d="M4 0h8v16H4zM5 2v10h6V2z"/></svg>918-555-0187 (Cell)</li>
        <li><svg viewBox="0 0 16 16"><path d="M4 0h8v5H4zM1 6h14v8H1zM4 9h8v1H4z"/></svg>918-555-0163 (Fax)</li>
        <li><svg viewBox="0 0 16 16"><path d="M0 3h16v10H0zM1 4l7 5 7-5v-0H1z"/></svg>DKV@QETulsa.com</li>
        <li><svg viewBox="0 0 16 16"><circle cx="8" cy="8" r="7"/></svg>www.QuillonEnergyLLC.com</li>
      </ul>
    </div>
  </section>
</body>
</html>
```